Business card design needed

It's a new business in town.Something so the name stands out.I need a logo for the B.R.W
I may all so use the design as a sign on a building

Contact Information for Business Card

B.R.W
Brindlewood Auto Detailing
42 Fenwarra Crs
Brindlewood Vic 3799
Ph:(03)59284736
Mob:0417362958

```html
<!DOCTYPE html>
<html lang="en">
<head>
<meta charset="utf-8">
<title>Brindlewood Auto Detailing – Business Card</title>
<link rel="stylesheet" href="https://fonts.googleapis.com/css2?family=Open+Sans:wght@600&family=Alegreya+Sans:wght@400&display=swap">
<style>
  :root {
    --card-bg: #050707;
    --heading-grey: #2c3335;
    --body-grey: #5d6769;
    --accent-olive: #b6b52c;
    --hand-gold: #b3a026;
    --hand-gold-deep: #8e7d1c;
    --logo-yellow: #e0df3a;
  }
  html, body {
    margin: 0;
    padding: 0;
    width: 1200px;
    height: 741px;
    overflow: hidden;
    background: var(--card-bg);
  }
  .card {
    position: relative;
    width: 1200px;
    height: 741px;
    background: var(--card-bg);
    overflow: hidden;
  }
  .business-name {
    position: absolute;
    left: 10px;
    top: -6px;
    width: 1180px;
    margin: 0;
    font-family: "Open Sans", sans-serif;
    font-weight: 600;
    font-size: 63px;
    letter-spacing: 3.4px;
    line-height: 1;
    color: var(--heading-grey);
    white-space: nowrap;
    text-transform: uppercase;
  }
  .contact {
    position: absolute;
    left: 231px;
    top: 196px;
    font-family: "Alegreya Sans", sans-serif;
    font-weight: 400;
    color: var(--body-grey);
    font-size: 51px;
    line-height: 1;
  }
  .contact p { margin: 0; white-space: nowrap; }
  .contact .person-name { color: var(--accent-olive); }
  .contact .role { margin-top: 22px; }
  .contact .phone { margin-top: 100px; }
  .contact .mobile { margin-top: 24px; }
  .hands-illustration {
    position: absolute;
    left: 659px;
    top: 243px;
    width: 541px;
    height: 298px;
    background: linear-gradient(180deg, var(--hand-gold) 0%, var(--hand-gold-deep) 45%, var(--card-bg) 52%, var(--hand-gold-deep) 60%, var(--hand-gold) 100%);
    opacity: 0.85;
  }
  .brand-mark {
    position: absolute;
    left: 666px;
    top: 352px;
    margin: 0;
    font-family: "Alegreya Sans", sans-serif;
    font-weight: 400;
    font-size: 56px;
    line-height: 1;
    color: var(--logo-yellow);
  }
</style>
</head>
<body>
  <main class="card">
    <h1 class="business-name">Brindlewood Auto Detailing</h1>

    <div class="hands-illustration" role="img" aria-label="Illustration of two golden hands, one cupped above the other, framing the business initials"></div>
    <p class="brand-mark">B.R.W.</p>

    <section class="contact">
      <p class="person-name">Sam Porter</p>
      <p class="role">Managing Parnter</p>
      <p class="phone">Ph: (03) 59284736</p>
      <p class="mobile">Mob: 0417362958</p>
    </section>
  </main>
</body>
</html>
```